Brightholm painting

Am looking for a lawn sign design for my paintings company.
I also attached my business card a example

Phone number of the business +1(431)572-8846
Key words:Free estimates|pressure washing |Residential| Commercial | Interior | Exterior

```html
<!DOCTYPE html>
<html lang="en">
<head>
<meta charset="utf-8">
<title>Brightholm Painting – Lawn Sign</title>
<link rel="stylesheet" href="https://fonts.googleapis.com/css2?family=Roboto+Condensed:wght@700&family=PT+Sans:ital@1&display=swap">
<style>
  :root {
    --ink: #000000;
    --band: #e6e7e8;
    --ring: #a7a9ac;
    --accent-green: #3cb44a;
    --brand-blue: #0aa4dc;
    --service-yellow: #f7e718;
    --rule: #8a8a8a;
    --white: #ffffff;
    --glow: #8a3f12;
    --grass-light: #b7e52a;
    --grass-mid: #4fb51f;
    --grass-dark: #1f6d2a;
    --sun: #e3812b;
  }
  * { margin: 0; padding: 0; box-sizing: border-box; }
  html, body { width: 1200px; height: 900px; overflow: hidden; background: var(--ink); }
  .sign {
    position: relative;
    width: 1200px;
    height: 900px;
    background: var(--ink);
    overflow: hidden;
    font-family: "Roboto Condensed", "Arial Narrow", sans-serif;
  }
  .sign-backdrop { position: absolute; inset: 0; width: 1200px; height: 900px; }
  .info-column {
    position: absolute;
    left: 700px;
    width: 450px;
    top: 0;
    height: 900px;
    text-align: center;
  }
  .brand-name {
    position: absolute;
    left: 0; right: 0;
    top: 146px;
    color: var(--brand-blue);
    font-weight: 700;
    text-transform: uppercase;
    line-height: 1;
  }
  .brand-name .brand-line-1 { display: block; font-size: 70px; letter-spacing: 3px; }
  .brand-name .brand-line-2 { display: block; font-size: 44px; letter-spacing: 17px; margin-top: 10px; padding-left: 17px; }
  .service-list {
    position: absolute;
    left: 69px;
    width: 312px;
    top: 324px;
    list-style: none;
  }
  .service-list li {
    color: var(--service-yellow);
    font-weight: 700;
    font-size: 44px;
    line-height: 62px;
    height: 62.5px;
    border-bottom: 1px solid var(--rule);
    white-space: nowrap;
  }
  .service-list li:last-child { border-bottom: none; }
  .call-prompt {
    position: absolute;
    left: 0; right: 0;
    top: 753px;
    color: var(--white);
    font-family: "PT Sans", "Trebuchet MS", sans-serif;
    font-style: italic;
    font-size: 18px;
  }
  .phone {
    position: absolute;
    left: 0; right: 0;
    top: 778px;
    color: var(--white);
    font-weight: 700;
    font-size: 56px;
    letter-spacing: -1px;
    line-height: 1;
  }
</style>
</head>
<body>
<main class="sign">
  <svg class="sign-backdrop" viewBox="0 0 2212 1659" aria-hidden="true">
    <defs>
      <radialGradient id="panel-glow" cx="1230" cy="830" r="620" gradientUnits="userSpaceOnUse">
        <stop offset="0" stop-color="var(--glow)" stop-opacity="0.9"/>
        <stop offset="0.5" stop-color="var(--glow)" stop-opacity="0.25"/>
        <stop offset="1" stop-color="var(--ink)" stop-opacity="0"/>
      </radialGradient>
      <linearGradient id="lawn-tones" x1="0" y1="0" x2="0" y2="1">
        <stop offset="0" stop-color="var(--sun)"/>
        <stop offset="0.22" stop-color="#b0705e"/>
        <stop offset="0.34" stop-color="var(--grass-mid)"/>
        <stop offset="0.65" stop-color="var(--grass-dark)"/>
        <stop offset="1" stop-color="var(--grass-light)"/>
      </linearGradient>
    </defs>
    <path class="curved-band" fill="var(--band)"
          d="M750,0 C480,420 480,1240 750,1659 L1450,1659 C920,1250 920,410 1450,0 Z"/>
    <path class="info-panel" fill="url(#panel-glow)"
          d="M1450,0 C920,410 920,1250 1450,1659 L2212,1659 L2212,0 Z"/>
    <path class="panel-edge" fill="none" stroke="var(--accent-green)" stroke-width="9"
          d="M1450,0 C920,410 920,1250 1450,1659"/>
    <circle class="photo-ring" cx="668" cy="830" r="590" fill="var(--ring)"/>
    <circle class="lawn-photo" cx="668" cy="830" r="545" fill="url(#lawn-tones)"
            role="img" aria-label="Close-up photo of fresh green lawn grass in sunlight"/>
  </svg>

  <section class="info-column">
    <h1 class="brand-name">
      <span class="brand-line-1">Brightholm</span>
      <span class="brand-line-2">Painting</span>
    </h1>
    <ul class="service-list">
      <li>Free Estimates</li>
      <li>Pressure Washing</li>
      <li>Residential</li>
      <li>Commercial</li>
      <li>Interior</li>
      <li>Exterior</li>
    </ul>
    <p class="call-prompt">Call to find out more</p>
    <p class="phone">+1(431)572-8846</p>
  </section>
</main>
</body>
</html>
```